World's toughest ocean race needs a spectacular flyer design

We are competing in the world's toughest ocean rowing race, the Pellmore Cider Trophy, see websites at http://www.pellmoreciderbrenvaltrophy.com
and
http://www.brisvendoutings.com/

Our team, is called Crew Velharra, see website at
http://crewvelharra.com

We need a flyer to promote our participation in the race and to drive our sponsorship efforts. Our likely sponsors will be corporations and as such the flyer needs to promote a professional image whilst also being somewhat edgy and exuberant to reflect the highly challenging nature of the race. The flyer should promote a sense of adventure and appeal to corporations who want to align themselves to challenging ventures. The flyer should most definitely not be dull!

The flyer should contain enough information to promote interest from potential sponsors which we will then follow up with personally. The flyer should be in at least 2 parts (perhaps even 2 separate flyers) . Part one will contain strong imagery and primarily contain details about the race itself and some information about our team. Part two will go into more detail about our fundraising efforts, an overview of sponsorship opportunities, personal information (brief biographies) about our team members etc. The flyer should be suitable for email distribution and print.

Following this project, the successful designer might be asked to produce additional flyers or material related to our sponsorship packages (but this should not be taken as a guarantee of future work)

```html
<!DOCTYPE html>
<html lang="en">
<head>
<meta charset="utf-8">
<title>Crew Velharra – Sponsorship Flyer</title>
<link href="https://fonts.googleapis.com/css2?family=Courier+Prime:wght@700&family=Stardos+Stencil:wght@700&display=swap" rel="stylesheet">
<style>
  :root {
    --page: #e9e6e1;
    --ink: #141414;
    --sky-top: #8fb4e0;
    --sky-mid: #d6e4f3;
    --horizon: #eef3f8;
    --sea-deep: #3d6fa8;
    --sea-mid: #7a9fca;
    --sea-fade: #f4f7fb;
    --frame: #f1e6c4;
    --frame-edge: #d8c999;
    --photo-sea: #5a7590;
    --photo-night: #3a2a28;
    --brand-navy: #0f2d52;
    --brand-blue: #1d5fa8;
  }
  * { margin: 0; padding: 0; box-sizing: border-box; }
  html, body { width: 1200px; height: 1000px; overflow: hidden; background: var(--page); }
  body { position: relative; font-family: "Courier Prime", "Courier New", monospace; color: var(--ink); }

  .flyer {
    position: absolute; left: 240px; top: 20px; width: 720px; height: 960px;
    overflow: hidden; box-shadow: 0 6px 18px rgba(0,0,0,.25);
  }
  .flyer__backdrop {
    position: absolute; inset: 0;
    background: linear-gradient(180deg,
      var(--sky-top) 0%, var(--sky-mid) 28%, var(--horizon) 43.5%,
      var(--sea-deep) 43.7%, var(--sea-mid) 62%, var(--sea-fade) 86%, #fff 100%);
  }

  .title {
    position: absolute; font-family: "Stardos Stencil", "Courier New", monospace;
    font-weight: 700; font-size: 70px; letter-spacing: 2px; line-height: 1;
    color: var(--ink); text-transform: uppercase; white-space: nowrap;
  }
  .title--first { left: 30px; top: 8px; }
  .title--second { left: 330px; top: 68px; }

  .block { position: absolute; font-weight: 700; text-transform: uppercase; white-space: nowrap; }
  .block__label { font-size: 21px; letter-spacing: 1px; margin-bottom: 10px; }
  .block__text { font-size: 22px; line-height: 1.2; letter-spacing: 1px; }

  .block--objective { left: 35px; top: 132px; }
  .block--participants { left: 260px; top: 325px; }
  .block--needed { left: 25px; top: 512px; }
  .block--needed .block__text { font-size: 24px; }
  .block--contact { left: 22px; top: 690px; }
  .block--contact .block__text { font-size: 28px; }

  .snapshot {
    position: absolute; background: var(--frame); border: 1px solid var(--frame-edge);
    padding: 12px; box-shadow: 3px 4px 6px rgba(0,0,0,.35);
  }
  .snapshot__image { width: 100%; height: 100%; }
  .snapshot--boat { left: 470px; top: 130px; width: 235px; height: 205px; }
  .snapshot--boat .snapshot__image { background: linear-gradient(160deg, #7f95aa, var(--photo-sea) 55%, #3f5870); }
  .snapshot--crew { left: 25px; top: 305px; width: 210px; height: 170px; }
  .snapshot--crew .snapshot__image { background: linear-gradient(180deg, var(--photo-night), #8a4a44 70%, #b58b7a); }

  .partners {
    position: absolute; left: 0; right: 0; top: 830px; height: 110px;
    display: flex; align-items: center; justify-content: space-between; padding: 0 16px;
  }
  .partner { font-weight: 700; text-transform: uppercase; }
  .partner--charity {
    border: 2px solid var(--brand-navy); padding: 8px 10px; color: var(--brand-navy);
    font-size: 15px; line-height: 1.15; width: 200px; text-align: center;
  }
  .partner--race {
    background: var(--brand-navy); color: #fff; width: 210px; height: 110px;
    display: flex; align-items: center; justify-content: center; text-align: center;
    font-size: 22px; line-height: 1.15; padding: 10px;
  }
  .partner--organiser {
    color: var(--brand-blue); font-size: 28px; line-height: 1.05; width: 230px; text-align: center;
  }
</style>
</head>
<body>
  <article class="flyer">
    <div class="flyer__backdrop" role="img" aria-label="Photograph of open ocean under a pale blue sky"></div>

    <h1 class="title title--first">Crew</h1>
    <h1 class="title title--second">Velharra</h1>

    <section class="block block--objective">
      <h2 class="block__label">Objective:</h2>
      <p class="block__text">Compete in the world's<br>toughest rowing race<br>across the Atlantic.</p>
    </section>

    <figure class="snapshot snapshot--boat">
      <div class="snapshot__image" role="img" aria-label="Photo of the crew rowing their boat on rough seas"></div>
    </figure>

    <figure class="snapshot snapshot--crew">
      <div class="snapshot__image" role="img" aria-label="Photo of crew members celebrating wrapped in flags"></div>
    </figure>

    <section class="block block--participants">
      <h2 class="block__label">Participants:</h2>
      <p class="block__text">Four men who are<br>fighting for a good<br>(and personal) cause.</p>
    </section>

    <section class="block block--needed">
      <h2 class="block__label">Needed:</h2>
      <p class="block__text">Your help! Help drive our efforts<br>by contributing to our charity or<br>sponsoring our challenge!</p>
    </section>

    <section class="block block--contact">
      <p class="block__text">Contact Dorian or Felix:<br>555-018-4472</p>
    </section>

    <footer class="partners">
      <div class="partner partner--charity">Harrowgate Men's Health Fund</div>
      <div class="partner partner--race">Pellmore Cider Trophy</div>
      <div class="partner partner--organiser">Brisvend Outings</div>
    </footer>
  </article>
</body>
</html>
```